Beauty Salon
I would like to see designs using sky blue and a soft orange. Mainly I would like my name ( Glow N' Wave Salon ) used as the design

Industry/Entity Type

Business

Contact Information for Business Card

Glow N'Wave Salon
418 E Maple Dr #14
Lakemont, Ca 95555
555 555-0172

```html
<!DOCTYPE html>
<html lang="en">
<head>
<meta charset="utf-8">
<title>Glow N' Wave Salon – Business Card</title>
<link href="https://fonts.googleapis.com/css2?family=Montserrat:wght@400;600&display=swap" rel="stylesheet">
<style>
  :root {
    --page-bg: #e9eaec;
    --card-bg: #ffffff;
    --card-edge: #d6d8db;
    --sky-blue: #3aa6dc;
    --soft-orange: #f08a2c;
    --ink: #55585c;
    --ink-soft: #6b6e72;
  }
  * { margin: 0; padding: 0; box-sizing: border-box; }
  html, body {
    width: 1200px;
    height: 970px;
    overflow: hidden;
    background: var(--page-bg);
    font-family: "Montserrat", Arial, sans-serif;
  }
  .canvas {
    position: relative;
    width: 1200px;
    height: 970px;
  }
  .business-card {
    position: absolute;
    left: 100px;
    top: 207px;
    width: 1000px;
    height: 556px;
    background: var(--card-bg);
    border: 1px solid var(--card-edge);
    border-radius: 22px;
    overflow: hidden;
    box-shadow: 0 18px 40px rgba(0, 0, 0, 0.12);
  }
  .brand {
    position: absolute;
    left: 50px;
    top: 108px;
  }
  .brand-name {
    font-weight: 600;
    font-size: 52px;
    line-height: 1;
    color: var(--soft-orange);
    letter-spacing: 0.5px;
  }
  .brand-tagline {
    margin-top: 22px;
    font-weight: 400;
    font-size: 27px;
    letter-spacing: 11px;
    color: var(--ink);
    text-transform: uppercase;
  }
  .contact {
    position: absolute;
    left: 72px;
    top: 318px;
    color: var(--ink-soft);
    font-size: 27px;
    font-style: normal;
    line-height: 1.45;
  }
  .contact-phone {
    display: flex;
    align-items: center;
    gap: 10px;
    margin-bottom: 18px;
  }
  .phone-icon { width: 26px; height: 22px; fill: var(--sky-blue); }
  .hair-illustration {
    position: absolute;
    right: 0;
    top: 0;
    width: 640px;
    height: 556px;
  }
</style>
</head>
<body>
<main class="canvas">
  <section class="business-card">
    <div class="brand">
      <p class="brand-name">Glow N' Wave</p>
      <p class="brand-tagline">Beauty Salon</p>
    </div>

    <address class="contact">
      <p class="contact-phone">
        <svg class="phone-icon" viewBox="0 0 26 22" aria-hidden="true">
          <path d="M2 7c0-3 5-5 11-5s11 2 11 5v2h-6V7c-1-1-9-1-10 0v2H2z"/>
          <path d="M7 10h12l4 10H3z"/>
        </svg>
        <span>555 555-0172</span>
      </p>
      <p>418 E Maple Dr #14</p>
      <p>Lakemont, Ca 95555</p>
    </address>

    <svg class="hair-illustration" viewBox="0 0 640 556" role="img"
         aria-label="Illustration of a woman's profile with long flowing hair in sky blue and soft orange layers">
      <defs>
        <linearGradient id="hairTones" x1="0" y1="0" x2="1" y2="1">
          <stop offset="0" stop-color="#f5a55a"/>
          <stop offset="0.5" stop-color="#5bb6e2"/>
          <stop offset="1" stop-color="#f08a2c"/>
        </linearGradient>
      </defs>
      <path d="M400 0 H520 C560 80 600 160 612 260 C626 380 604 480 590 556 H40
               C150 530 300 520 380 440 C440 370 420 260 410 160 C404 90 396 40 400 0 Z"
            fill="url(#hairTones)" opacity="0.9"/>
    </svg>
  </section>
</main>
</body>
</html>
```